Brindle Structures Construction Company Seeking Modern Website

We are a small construction company wanting to create a web presence. We don't have much in the way of current content but will get photos as they come in. Attached is a picture of our business card.
The pages we would like on the menu are:
Home
Portfolio
Product Specs
Testimonials
Our Process
Contact
Some designs we like are:
http://www.tovenquarnsheds.example/
http://www.qzrsheds.example/
http://pannowsheds.example/
http://wistenhalls.example/
Not much requirements other than that so feel free to be creative!
Updates
Target Market(s)
Construction
Commercial and Residential Buildings
Industry/Entity Type
Construction Company
Number of Pages Required
5+ page
Look and feel

```html
<!DOCTYPE html>
<html lang="en">
<head>
<meta charset="utf-8">
<title>Brindle Structures — Building Dreams</title>
<link rel="stylesheet" href="https://fonts.googleapis.com/css2?family=Noto+Serif:wght@400;700&display=swap">
<style>
  :root {
    --red: #d6281f;
    --sky: #00a6df;
    --sky-light: #18b4ea;
    --deep-blue: #0f63c4;
    --teal-title: #1b6f9e;
    --link-blue: #1a6ea0;
    --ink: #1d1d1d;
    --muted: #555;
    --rule: #c8c8c8;
    --footer-bg: #eeeeee;
    --white: #ffffff;
  }
  * { box-sizing: border-box; margin: 0; padding: 0; }
  html, body { width: 1200px; height: 2299px; overflow: hidden; }
  body { position: relative; background: var(--white); font-family: "Noto Serif", Georgia, serif; color: var(--ink); }
  .abs { position: absolute; }

  .top-rule { left: 0; top: 0; width: 1200px; height: 6px; background: var(--red); }

  .main-nav a { position: absolute; top: 50px; font-size: 13px; color: var(--ink); text-decoration: none; letter-spacing: .2px; }
  .main-nav a.is-active { color: var(--sky); }
  .brand { left: 500px; top: 40px; width: 200px; height: 38px; display: flex; align-items: center; justify-content: center; font-size: 22px; font-weight: 700; color: var(--red); }

  .hero { left: 173px; top: 107px; width: 854px; height: 408px; background: linear-gradient(135deg, #c9b28c 0%, #e3d6c2 45%, #b9b3aa 100%); }
  .hero-caption { left: 0; bottom: 0; width: 100%; height: 91px; background: rgba(20,20,20,.78); }
  .hero-title { left: 19px; top: 20px; font-size: 31px; color: var(--white); }
  .hero-sub { left: 19px; top: 57px; font-size: 14px; color: #e6e6e6; }
  .hero-dots { right: 34px; top: 40px; display: flex; gap: 7px; }
  .hero-dots span { width: 9px; height: 9px; border-radius: 50%; background: var(--white); }

  .focus { left: 0; top: 555px; width: 1200px; height: 447px; background: var(--sky); }
  .focus h2 { position: absolute; top: 44px; width: 100%; text-align: center; font-weight: 400; font-size: 27px; color: var(--white); }
  .focus-card { top: 110px; width: 416px; }
  .focus-photo { position: relative; height: 218px; }
  .focus-label { position: absolute; left: 0; bottom: 0; width: 100%; height: 46px; background: rgba(15,15,15,.72); color: var(--white); font-size: 18px; padding: 11px 18px; }
  .focus-label .go { position: absolute; right: 16px; top: 14px; }
  .focus-text { margin-top: 22px; font-size: 10.5px; line-height: 18px; color: var(--white); }

  .portfolio-title { left: 0; top: 1036px; width: 1200px; text-align: center; font-weight: 400; font-size: 27px; color: var(--teal-title); }
  .portfolio-rule { left: 173px; top: 1099px; width: 854px; height: 2px; background: var(--rule); }
  .project { width: 270px; }
  .project-photo { height: 187px; }
  .project-meta { position: relative; margin-top: 22px; height: 40px; }
  .project-name { font-size: 13.5px; color: var(--link-blue); line-height: 18px; }
  .project-place { font-size: 13.5px; color: #333; line-height: 18px; }
  .more-btn { position: absolute; right: 0; top: -5px; width: 90px; height: 28px; background: var(--red); color: var(--white); font-size: 10px; display: flex; align-items: center; justify-content: center; letter-spacing: .3px; }

  .testimonials { left: 0; top: 1744px; width: 1200px; height: 353px; overflow: hidden; }
  .testimonial-scene { left: 0; top: 0; width: 1200px; height: 353px; background: linear-gradient(90deg, #8a8a8a 0%, #cfcfcf 30%, #e4e4e4 55%, #9b9b9b 75%, #d9d9d9 100%); }
  .testimonial-shape { left: 0; top: 0; }
  .testimonial-body { left: 270px; top: 0; width: 300px; text-align: center; color: var(--white); }
  .testimonial-body h2 { margin-top: 78px; font-weight: 400; font-size: 28px; }
  .testimonial-quote { margin-top: 22px; font-size: 10.5px; line-height: 17.5px; }
  .testimonial-name { margin-top: 16px; font-size: 23px; }
  .testimonial-name .mark { font-size: 40px; font-weight: 700; vertical-align: -10px; margin-right: 4px; }
  .testimonial-role { margin-top: 2px; font-size: 10px; }
  .slider-arrow { top: 158px; }

  .site-footer { left: 0; top: 2097px; width: 1200px; height: 202px; background: var(--footer-bg); }
  .pill { top: 44px; width: 180px; height: 28px; border-radius: 14px; background: var(--red); color: var(--white); font-size: 13px; display: flex; align-items: center; justify-content: center; }
  .social { left: 437px; top: 47px; display: flex; gap: 8px; }
  .social span { width: 22px; height: 22px; border-radius: 50%; border: 1px solid #9a9a9a; }
  .newsletter-input { left: 812px; top: 44px; width: 211px; height: 28px; background: var(--white); border-radius: 0 14px 14px 0; font-size: 8.5px; color: #777; padding: 9px 0 0 15px; }
  .go-btn { right: 4px; top: 3px; width: 22px; height: 22px; border-radius: 50%; background: #2a2a2a; color: var(--white); font-size: 8px; display: flex; align-items: center; justify-content: center; }
  .footer-rule { left: 0; top: 95px; width: 1200px; height: 1px; background: #dcdcdc; }
  .footer-nav a { position: absolute; top: 120px; font-size: 13px; color: var(--ink); text-decoration: none; }
  .copyright { left: 0; top: 157px; width: 1200px; text-align: center; font-size: 13px; }
</style>
</head>
<body>
  <div class="abs top-rule"></div>

  <nav class="main-nav">
    <a class="is-active" style="left:191px">HOME</a>
    <a style="left:265px">PORTFOLIO</a>
    <a style="left:359px">PRODUCT SPECS</a>
    <a style="left:714px">TESTIMONIALS</a>
    <a style="left:843px">OUR PROCESS</a>
    <a style="left:950px">CONTACT</a>
  </nav>
  <div class="abs brand">Brindle Structures</div>

  <section class="abs hero" role="img" aria-label="Builder in hard hat and safety vest drilling inside a timber-framed house">
    <div class="abs hero-caption">
      <div class="abs hero-title">Building Dreams</div>
      <div class="abs hero-sub">so you can dream your memories</div>
      <div class="abs hero-dots"><span></span><span></span><span></span><span></span></div>
    </div>
  </section>

  <section class="abs focus">
    <h2>What We Focus ?</h2>
    <article class="abs focus-card" style="left:173px">
      <div class="focus-photo" role="img" aria-label="City skyline with cranes over towers at dusk" style="background:linear-gradient(180deg,#2b4f9e 0%,#5c7fc8 55%,#3a3020 100%)">
        <div class="focus-label">Commercial Construction
          <svg class="go" width="18" height="18" viewBox="0 0 18 18"><circle cx="9" cy="9" r="9" fill="#fff"/><path d="M7.5 5l4 4-4 4" stroke="#222" stroke-width="2" fill="none"/></svg>
        </div>
      </div>
      <p class="focus-text">Lorem Ipsum is simply dummy text of the printing and typesetting industry. Lorem Ipsum has been the industry's standard dummy text ever since the 1500s, when an unknown printer took a galley of type and scrambled</p>
    </article>
    <article class="abs focus-card" style="left:611px">
      <div class="focus-photo" role="img" aria-label="Modern two-storey house lit up at dusk" style="background:linear-gradient(180deg,#3e5a3a 0%,#8d93a0 45%,#5a4a38 100%)">
        <div class="focus-label">Residential Buildings
          <svg class="go" width="18" height="18" viewBox="0 0 18 18"><circle cx="9" cy="9" r="9" fill="#fff"/><path d="M7.5 5l4 4-4 4" stroke="#222" stroke-width="2" fill="none"/></svg>
        </div>
      </div>
      <p class="focus-text">Lorem Ipsum is simply dummy text of the printing and typesetting industry. Lorem Ipsum has been the industry's standard dummy text ever since the 1500s, when an unknown printer took a galley of type and scrambled</p>
    </article>
  </section>

  <h2 class="abs portfolio-title">Portfolio</h2>
  <div class="abs portfolio-rule"></div>

  <article class="abs project" style="left:173px;top:1136px">
    <div class="project-photo" role="img" aria-label="Blue-roofed family house behind a green lawn" style="background:linear-gradient(180deg,#9cc3e6 0%,#4f7a4a 55%,#8aa56a 100%)"></div>
    <div class="project-meta"><div class="project-name">Residential Buildings</div><div class="project-place">Australia, Sydney</div><div class="more-btn">MORE INFO</div></div>
  </article>
  <article class="abs project" style="left:466px;top:1136px">
    <div class="project-photo" role="img" aria-label="Suburban house with a wide lawn and flower beds" style="background:linear-gradient(180deg,#a9cbe8 0%,#c9bfae 40%,#5f9a3a 100%)"></div>
    <div class="project-meta"><div class="project-name">Residential Buildings</div><div class="project-place">Australia, Sydney</div><div class="more-btn">MORE INFO</div></div>
  </article>
  <article class="abs project" style="left:757px;top:1136px">
    <div class="project-photo" role="img" aria-label="Row of gabled houses with garden beds" style="background:linear-gradient(180deg,#b7d0e6 0%,#8c8a80 45%,#4f8a34 100%)"></div>
    <div class="project-meta"><div class="project-name">Residential Buildings</div><div class="project-place">Australia, Sydney</div><div class="more-btn">MORE INFO</div></div>
  </article>

  <article class="abs project" style="left:173px;top:1433px">
    <div class="project-photo" role="img" aria-label="Glass-walled modern house interior" style="background:linear-gradient(135deg,#e9e2c8 0%,#f3f3ef 50%,#b8bdb5 100%)"></div>
    <div class="project-meta"><div class="project-name">Residential Buildings</div><div class="project-place">Australia, Sydney</div><div class="more-btn">MORE INFO</div></div>
  </article>
  <article class="abs project" style="left:466px;top:1433px">
    <div class="project-photo" role="img" aria-label="Villa with palm trees and a blue swimming pool" style="background:linear-gradient(180deg,#4c86c8 0%,#3f6a3a 40%,#2fb4e0 75%,#d8cdb8 100%)"></div>
    <div class="project-meta"><div class="project-name">Residential Buildings</div><div class="project-place">Australia, Sydney</div><div class="more-btn">MORE INFO</div></div>
  </article>
  <article class="abs project" style="left:757px;top:1433px">
    <div class="project-photo" role="img" aria-label="Brick townhouses along a tree-lined path" style="background:linear-gradient(180deg,#8dbbe8 0%,#b46a45 50%,#5c8f3c 100%)"></div>
    <div class="project-meta"><div class="project-name">Residential Buildings</div><div class="project-place">Australia, Sydney</div><div class="more-btn">MORE INFO</div></div>
  </article>

  <section class="abs testimonials">
    <div class="abs testimonial-scene" role="img" aria-label="Black and white scaffolding with a bearded builder in a hard hat on the right"></div>
    <svg class="abs testimonial-shape" width="1200" height="353" viewBox="0 0 1200 353">
      <polygon points="168,0 674,0 630,353 200,353" fill="#1aa8e4"/>
      <polygon points="290,0 575,0 620,353 240,353" fill="#0d62c8"/>
    </svg>
    <div class="abs testimonial-body">
      <h2>Testimonials</h2>
      <p class="testimonial-quote">Lorem Ipsum is simply dummy text of the printing and typesetting industry. Lorem Ipsum has been the industry's standard dummy text ever since the 1500s, when an unknown printer took a galley of type and scrambled it to make a type specimen book.</p>
      <div class="testimonial-name"><span class="mark">&ldquo;</span>Darren Holt</div>
      <div class="testimonial-role">Building Supervisor</div>
    </div>
    <svg class="abs slider-arrow" style="left:114px" width="42" height="42" viewBox="0 0 42 42"><circle cx="21" cy="21" r="19" fill="rgba(255,255,255,.4)" stroke="#333" stroke-width="2"/><path d="M25 12l-10 9 10 9z" fill="#333"/></svg>
    <svg class="abs slider-arrow" style="left:1055px" width="42" height="42" viewBox="0 0 42 42"><circle cx="21" cy="21" r="19" fill="rgba(255,255,255,.4)" stroke="#333" stroke-width="2"/><path d="M17 12l10 9-10 9z" fill="#333"/></svg>
  </section>

  <footer class="abs site-footer">
    <div class="abs pill" style="left:219px">Connect With Us</div>
    <div class="abs social"><span></span><span></span><span></span><span></span><span></span></div>
    <div class="abs pill" style="left:638px">Newsletter Sign Up</div>
    <div class="abs newsletter-input">Enter Your E-Mail Address<div class="abs go-btn">GO</div></div>
    <div class="abs footer-rule"></div>
    <nav class="footer-nav">
      <a style="left:300px">HOME</a>
      <a style="left:372px">PORTFOLIO</a>
      <a style="left:467px">PRODUCT SPECS</a>
      <a style="left:601px">TESTIMONIALS</a>
      <a style="left:730px">OUR PROCESS</a>
      <a style="left:837px">CONTACT</a>
    </nav>
    <div class="abs copyright">&copy; 2015 COMPANY NAME &nbsp;|&nbsp; ALL RIGHTS RESERVED</div>
  </footer>
</body>
</html>
```